Conversion Optimisation Checklist for eCommerce websites

We need a design for a 2 page pdf checklist (attached document outline), the first page is checklist. Document will be primarly for digital viewing - don't need to worry about print. Should have our website address (torvo.com.au), email (hello@torvo.com.au) and phone number (1300 482 917) in the footer
The second page is a bonus, a wireframe of an ecommerce homepage with annotations to show what information is important where.
Should be branded with our branding (logo attached) and compliment the design (colours/style/imagery) of an accompanying landing page design (attached).

We are a website and marketing agency thank helps young ecommerce businesses to grow faster.

```html
<!DOCTYPE html>
<html lang="en">
<head>
<meta charset="utf-8">
<title>Torvo Interactive – Lead Magnet Checklist</title>
<link rel="stylesheet" href="https://fonts.googleapis.com/css2?family=Montserrat:wght@400;500;700&family=Permanent+Marker&display=swap">
<style>
:root{
  --backdrop:#6e6e6e;
  --navy:#10243a;
  --navy-2:#1f4258;
  --blue:#2f8fd6;
  --blue-dark:#1f74b8;
  --text:#3c4650;
  --paper:#ffffff;
  --wire-grey:#e6e8ea;
  --wire-block:#d6d8da;
  --hill-1:#a9c9cc;
  --hill-2:#5f8fa6;
}
*{box-sizing:border-box;margin:0;padding:0}
html,body{width:1200px;height:888px;overflow:hidden;background:var(--backdrop);font-family:"Montserrat",sans-serif;color:var(--text)}
.page{position:absolute;top:86px;width:509px;height:718px;background:var(--paper);overflow:hidden;box-shadow:0 4px 14px rgba(0,0,0,.35)}
.page--checklist{left:67px}
.page--wireframe{left:626px}
.abs{position:absolute}
.header{position:absolute;left:0;top:0;width:100%;background:linear-gradient(115deg,var(--navy) 40%,var(--navy-2))}
.brush{position:absolute;left:0;width:100%}
.brand{position:absolute;display:flex;align-items:center;gap:6px;color:#fff;font-weight:700;letter-spacing:.5px}
.brand__dot{width:14px;height:14px;border-radius:50%;background:var(--blue)}
.title{position:absolute;font-family:"Permanent Marker",cursive;color:#fff;letter-spacing:1px;line-height:1}
.subtitle{position:absolute;color:#fff;line-height:1.35}
.subtitle b{color:var(--blue);font-weight:700}
.devices{position:absolute;background:linear-gradient(160deg,#f4f6f8,#d9dde1);border-radius:6px}
.section-title{position:absolute;font-size:13.5px;font-weight:700;color:var(--blue-dark);display:flex;align-items:center;gap:6px}
.section-title::after{content:"";display:block;width:60px;height:1px;background:var(--blue);box-shadow:-4px 0 0 1px var(--blue) inset}
.item{position:absolute;width:200px;display:flex;gap:10px;font-size:8.6px;line-height:1.25}
.tick{flex:0 0 15px;height:15px;border-radius:50%;background:var(--blue-dark);position:relative}
.tick::after{content:"";position:absolute;left:4px;top:4.5px;width:4px;height:4px;border-right:1.5px solid #fff;border-top:1.5px solid #fff;transform:rotate(45deg)}
.hills{position:absolute;left:0;bottom:0;width:100%;background:linear-gradient(180deg,var(--hill-1),var(--hill-2))}
.engage-title{position:absolute;color:#fff;font-weight:700;font-size:13px;line-height:1.1}
.engage-item{position:absolute;width:150px;display:flex;gap:8px;color:#fff;font-size:8.6px;line-height:1.25}
.ring{flex:0 0 16px;height:16px;border-radius:50%;border:1px solid #fff;position:relative}
.ring::after{content:"";position:absolute;left:4px;top:5px;width:3px;height:3px;border-right:1px solid #fff;border-top:1px solid #fff;transform:rotate(45deg)}
.note{position:absolute;font-size:6.6px;line-height:1.25;color:var(--blue-dark)}
.note--left{text-align:right}
.pin{position:absolute;width:9px;height:9px;border:1px solid #c5cbd0;border-radius:50%}
.wire{position:absolute;background:var(--wire-grey)}
.wire--block{background:var(--wire-block)}
.wire--box{background:#f6f7f8;border:1px solid var(--blue)}
.wire--btn{background:var(--blue)}
.wire--outline{border:1px solid var(--blue);background:transparent}
.contact{position:absolute;top:694px;color:#fff;font-size:8px;font-weight:700;display:flex;align-items:center;gap:5px}
.contact svg{width:9px;height:9px}
</style>
</head>
<body>

<!-- Page 1: checklist -->
<section class="page page--checklist">
  <div class="header" style="height:232px"></div>
  <svg class="brush" style="top:205px;height:40px" viewBox="0 0 509 40" preserveAspectRatio="none">
    <path d="M0 18 L120 14 L260 6 L380 10 L509 4 L509 40 L0 40Z" fill="#fff"/>
    <path d="M0 20 L150 12 L300 6 L340 12 L300 14 L170 20 L60 26 L0 34Z" fill="var(--blue)"/>
  </svg>
  <div class="brand" style="left:45px;top:38px;font-size:15px"><span class="brand__dot"></span>TORVO</div>
  <div class="title" style="left:42px;top:124px;font-size:40px">LEAD MAGNET</div>
  <p class="subtitle" style="left:41px;top:188px;font-size:11px"><b>25-Step</b> Checklist to Optimise your<br>Website and Increase Sales Conversions</p>
  <div class="devices" role="img" aria-label="Laptop and phone showing an ecommerce storefront" style="left:352px;top:75px;width:157px;height:146px"></div>

  <div class="section-title" style="left:40px;top:254px">BE COMPELLING</div>
  <div class="item" style="left:40px;top:276px"><span class="tick"></span>Encourage purchases with featured products or sales</div>
  <div class="item" style="left:40px;top:303px"><span class="tick"></span>Draw attention to popular (or profitable) products</div>
  <div class="item" style="left:40px;top:330px"><span class="tick"></span>Clearly show discounted pricing and the benefit</div>
  <div class="item" style="left:40px;top:358px"><span class="tick"></span>Encourage purchases over a free shipping threshold</div>
  <div class="item" style="left:40px;top:385px"><span class="tick"></span>Make your site messaging reflect the key benefits your products provide</div>

  <div class="section-title" style="left:256px;top:254px">BUILD TRUST</div>
  <div class="item" style="left:256px;top:276px;width:215px"><span class="tick"></span>Includes your phone number on key areas people might have questions like the cart or checkout</div>
  <div class="item" style="left:256px;top:313px"><span class="tick"></span>Ensure your site uses a SSL certificate and loads over https</div>
  <div class="item" style="left:256px;top:340px"><span class="tick"></span>Offer different payment methods</div>
  <div class="item" style="left:256px;top:358px"><span class="tick"></span>Have a professional design</div>
  <div class="item" style="left:256px;top:385px;width:215px"><span class="tick"></span>Have all the information customers need including shipping, returns &amp; delivery policies</div>

  <div class="section-title" style="left:40px;top:425px">BE SIMPLE</div>
  <div class="item" style="left:40px;top:447px"><span class="tick"></span>Make navigation clear &amp; simple</div>
  <div class="item" style="left:40px;top:474px"><span class="tick"></span>Display products and their price clearly</div>
  <div class="item" style="left:40px;top:501px"><span class="tick"></span>Have additional information for products that need it</div>
  <div class="item" style="left:40px;top:529px"><span class="tick"></span>Use high quality images to show off your product</div>
  <div class="item" style="left:40px;top:556px"><span class="tick"></span>Ensure you have appropriate shipping methods setup for your customers</div>

  <div class="section-title" style="left:256px;top:425px">DRIVE TRAFFIC</div>
  <div class="item" style="left:256px;top:447px"><span class="tick"></span>Ensure your website is setup and optimised for search keywords</div>
  <div class="item" style="left:256px;top:474px"><span class="tick"></span>Ensure reporting &amp; tracking is in place</div>
  <div class="item" style="left:256px;top:501px"><span class="tick"></span>Consider paid marketing and measure your ROI through analytics</div>
  <div class="item" style="left:256px;top:529px"><span class="tick"></span>Regularly review reports</div>
  <div class="item" style="left:256px;top:556px"><span class="tick"></span>Build interesting and insightful content around your products</div>

  <div class="hills" role="img" aria-label="Misty blue mountain range" style="height:130px"></div>
  <div class="engage-title" style="left:42px;top:622px">ENGAGE YOUR<br>CUSTOMERS</div>
  <div class="engage-item" style="left:42px;top:664px;width:130px"><span class="ring"></span>Engage with customers on social media through related groups or pages</div>
  <div class="engage-item" style="left:183px;top:627px"><span class="ring"></span>Email customers that abandon their cart before purchasing</div>
  <div class="engage-item" style="left:183px;top:664px"><span class="ring"></span>Use email automation to follow up existing customers with offers or promotions</div>
  <div class="engage-item" style="left:351px;top:627px;width:130px"><span class="ring"></span>Reward loyal &amp; repeat customers</div>
  <div class="engage-item" style="left:351px;top:664px;width:130px"><span class="ring"></span>Setup a referral bonus for new customers</div>
</section>

<!-- Page 2: homepage wireframe -->
<section class="page page--wireframe">
  <div class="header" style="height:165px"></div>
  <svg class="brush" style="top:150px;height:34px" viewBox="0 0 509 34" preserveAspectRatio="none">
    <path d="M0 14 L140 8 L280 4 L509 0 L509 34 L0 34Z" fill="#fff"/>
    <path d="M0 16 L120 10 L230 8 L180 14 L80 22 L0 30Z" fill="var(--blue)"/>
  </svg>
  <div class="brand" style="left:36px;top:36px;font-size:12px"><span class="brand__dot" style="width:11px;height:11px"></span>TORVO</div>
  <div class="title" style="left:35px;top:88px;font-size:30px">LEAD MAGNET</div>
  <p class="subtitle" style="left:35px;top:126px;font-size:9px"><b>25-Step</b> Checklist to Optimise your<br>Website and Increase Sales Conversions</p>
  <div class="devices" role="img" aria-label="Laptop and phone showing an ecommerce storefront" style="left:334px;top:28px;width:175px;height:148px"></div>

  <p class="note" style="left:129px;top:210px">Home Page</p>
  <p class="note" style="left:236px;top:210px">Search bar</p>
  <p class="note" style="left:331px;top:210px">Currency display if multicurrency or<br>unclear to all traffic sources</p>
  <span class="pin" style="left:145px;top:229px"></span>
  <span class="pin" style="left:251px;top:229px"></span>
  <span class="pin" style="left:346px;top:229px"></span>

  <div class="wire" style="left:127px;top:243px;width:247px;height:375px"></div>
  <div class="wire wire--block" style="left:131px;top:258px;width:33px;height:14px"></div>
  <div class="wire wire--block" style="left:222px;top:258px;width:58px;height:14px"></div>
  <div class="wire wire--block" style="left:329px;top:258px;width:40px;height:14px"></div>
  <div class="wire wire--block" style="left:131px;top:276px;width:238px;height:10px"></div>
  <div class="wire wire--btn" style="left:140px;top:301px;width:84px;height:10px"></div>
  <div class="wire wire--btn" style="left:140px;top:315px;width:84px;height:10px"></div>
  <div class="wire wire--outline" style="left:140px;top:329px;width:32px;height:9px"></div>
  <div class="wire wire--block" style="left:131px;top:355px;width:238px;height:14px"></div>
  <div class="wire wire--box" style="left:131px;top:377px;width:70px;height:33px"></div>
  <div class="wire wire--box" style="left:214px;top:377px;width:70px;height:33px"></div>
  <div class="wire wire--box" style="left:297px;top:377px;width:71px;height:33px"></div>
  <div class="wire wire--box" style="left:131px;top:420px;width:56px;height:30px"></div>
  <div class="wire wire--box" style="left:131px;top:451px;width:56px;height:30px"></div>
  <div class="wire wire--box" style="left:187px;top:420px;width:127px;height:61px"></div>
  <div class="wire wire--box" style="left:314px;top:420px;width:54px;height:30px"></div>
  <div class="wire wire--box" style="left:314px;top:451px;width:54px;height:30px"></div>
  <div class="wire wire--box" style="left:131px;top:516px;width:56px;height:37px"></div>
  <div class="wire wire--box" style="left:191px;top:516px;width:56px;height:37px"></div>
  <div class="wire wire--box" style="left:251px;top:516px;width:56px;height:37px"></div>
  <div class="wire wire--box" style="left:311px;top:516px;width:57px;height:37px"></div>
  <div class="wire wire--block" style="left:131px;top:565px;width:237px;height:20px;background:#eceeef"></div>
  <div class="wire wire--block" style="left:131px;top:593px;width:52px;height:10px"></div>

  <p class="note note--left" style="right:401px;top:259px">Logo</p>
  <p class="note note--left" style="right:401px;top:274px">Simple Navigation<br>with cart</p>
  <p class="note note--left" style="right:401px;top:373px">Additional messaging<br>around returns or<br>special requirements</p>
  <p class="note note--left" style="right:401px;top:474px">Exit intent popup<br>with offer</p>
  <p class="note note--left" style="right:401px;top:535px">Information about your<br>business, why you exist<br>and why your customers<br>should care ideally with<br>a video</p>
  <p class="note note--left" style="right:401px;top:610px">Site purchase<br>activity dialog</p>
  <span class="pin" style="left:113px;top:260px"></span>
  <span class="pin" style="left:113px;top:277px"></span>
  <span class="pin" style="left:113px;top:380px"></span>
  <span class="pin" style="left:113px;top:478px"></span>
  <span class="pin" style="left:113px;top:551px"></span>
  <span class="pin" style="left:113px;top:614px"></span>

  <p class="note" style="left:398px;top:241px">Promotional<br>message bar</p>
  <p class="note" style="left:398px;top:264px">Unique message<br>potentially free ship-<br>ping or other USP of<br>your business</p>
  <p class="note" style="left:398px;top:315px">Key image with<br>messaging Outlining<br>more benefits of your<br>products<br>And call to action</p>
  <p class="note" style="left:398px;top:371px">Core Product<br>categories</p>
  <p class="note" style="left:398px;top:434px">Testimonial</p>
  <p class="note" style="left:398px;top:478px">Promotional product<br>or categories</p>
  <p class="note" style="left:398px;top:511px">Top selling products or<br>lastest to be reviewed<br>Showing star ratings<br>and price</p>
  <p class="note" style="left:398px;top:552px">Newsletter subscription<br>with offer if subscribed</p>
  <p class="note" style="left:398px;top:575px">Footer with customer care<br>information including<br>return &amp; delivery policy Trust<br>symbols like accepted cred-<br>it cards and/or SSL secure<br>badges</p>
  <span class="pin" style="left:384px;top:244px"></span>
  <span class="pin" style="left:384px;top:268px"></span>
  <span class="pin" style="left:384px;top:319px"></span>
  <span class="pin" style="left:384px;top:373px"></span>
  <span class="pin" style="left:384px;top:434px"></span>
  <span class="pin" style="left:384px;top:480px"></span>
  <span class="pin" style="left:384px;top:525px"></span>
  <span class="pin" style="left:384px;top:555px"></span>
  <span class="pin" style="left:384px;top:593px"></span>

  <div class="hills" role="img" aria-label="Misty blue mountain range" style="height:86px"></div>
  <p class="contact" style="left:98px">
    <svg viewBox="0 0 10 10"><rect x=".5" y="1.5" width="9" height="7" fill="none" stroke="#fff"/><path d="M.5 1.5 L5 5.5 L9.5 1.5" fill="none" stroke="#fff"/></svg>hello@torvo.com.au</p>
  <p class="contact" style="left:231px">
    <svg viewBox="0 0 10 10"><circle cx="5" cy="5" r="4.5" fill="none" stroke="#fff"/><path d="M3.5 3 L4.5 3 L5 4.5 L4.3 5 Q5 6.2 6 6.5 L6.5 5.8 L7.5 6.5 L7.2 7.3 Q4 7.2 3 3.8Z" fill="#fff"/></svg>1300 482 917</p>
  <p class="contact" style="left:341px">
    <svg viewBox="0 0 10 10"><circle cx="5" cy="5" r="4.5" fill="none" stroke="#fff"/><ellipse cx="5" cy="5" rx="2" ry="4.5" fill="none" stroke="#fff"/><path d="M.5 5 H9.5" stroke="#fff"/></svg>torvo.com.au</p>
</section>

</body>
</html>
```